Distinctive Men collection for beard oil, beard balm and hand cream

I have a project: a collection for MEN.
The name of my company is KELV.
- You can play with the writing of the name without any problem.
- I need a label template for my BEARD oil bottles (it needs to have a place where I can change the skin type: dry skin / normal skin / or oily skin)
- I need a round label template for the 50 ml beard balm for the top of the aluminium can. I would like to use something similar for the hand cream so it would fit.

Example of Ingredients:
Beard oil | Oily skin: Ingrédients : Simmondsia chinensis (Jojoba) Seed Oil *, Corylus avellana (Hazelnut) Oil*, Vitis vinifera Seed Oil*, Trocopherol, parfum.

It is a collection, it needs to fit together!

Thank you :-D

Target Market(s)

MEN with a beard

Colors

Designer to choose colors to be used in the design.

Requirements
Must have
• - Labels for the bottles: 1 3/4' X 4'
• - Round label for the beard balm and the hand cream for men: round 1 3/4'
• - For the bottles: the ingredients goes on one end on the label and the Expiration on the other end, so they are "behind" the bottle. Hope I'm clear, I'm not a desgner ;-)
Nice to have
• I have been looking at labels type, and I like the effect of transparent label on amber buttle, BUT it is not at all a must. Just an observation. I am really open to everything!
Should not have
• Important fact: I don't want black and white like almost every bottles on Brindle and in barbershop. I want them both to appeal to trendy barbers AND I want them on Brindle.

```html
<!DOCTYPE html>
<html lang="en">
<head>
<meta charset="utf-8">
<title>KELV Beard Oil Label</title>
<link rel="stylesheet" href="https://fonts.googleapis.com/css2?family=Arimo:wght@400;700&family=Oswald:wght@400;500;700&display=swap">
<style>
  :root {
    --paper: #ffffff;
    --band: #000000;
    --copper-light: #f6c9b0;
    --copper-mid: #e8a98c;
    --copper-deep: #c98467;
    --copper-rim: #a86a50;
    --ink: #141414;
    --label-text: #ffffff;
  }
  html, body {
    margin: 0;
    padding: 0;
    width: 1200px;
    height: 1000px;
    overflow: hidden;
    background: var(--paper);
  }
  .canvas {
    position: relative;
    width: 1200px;
    height: 1000px;
  }
  .bottle-label {
    position: absolute;
    left: 226px;
    top: 340px;
    width: 748px;
    height: 320px;
  }
  .bottle-label svg { display: block; }
  .band { fill: var(--band); }
  .oval-rim { fill: var(--band); }
  .oval-face { stroke: var(--copper-rim); stroke-width: 2; }
  .rule { stroke: var(--ink); stroke-width: 1.6; }
  .info-text {
    font-family: "Arimo", Arial, sans-serif;
    font-size: 13px;
    fill: var(--label-text);
  }
  .info-strong { font-weight: 700; }
  .brand-name {
    font-family: "Oswald", sans-serif;
    font-weight: 500;
    font-size: 44px;
    letter-spacing: 2px;
    fill: var(--ink);
  }
  .skin-type {
    font-family: "Oswald", sans-serif;
    font-weight: 400;
    font-size: 20px;
    letter-spacing: 1px;
    fill: var(--ink);
  }
  .product-name {
    font-family: "Oswald", sans-serif;
    font-weight: 700;
    font-size: 30px;
    letter-spacing: 0.5px;
    fill: var(--ink);
  }
  .volume {
    font-family: "Arimo", Arial, sans-serif;
    font-weight: 700;
    font-size: 12px;
    fill: var(--ink);
  }
</style>
</head>
<body>
<div class="canvas">
  <div class="bottle-label">
    <svg width="748" height="320" viewBox="0 0 748 320" xmlns="http://www.w3.org/2000/svg">
      <defs>
        <linearGradient id="copperFoil" x1="0" y1="0" x2="1" y2="1">
          <stop offset="0" stop-color="var(--copper-mid)"/>
          <stop offset="0.45" stop-color="var(--copper-light)"/>
          <stop offset="1" stop-color="var(--copper-deep)"/>
        </linearGradient>
      </defs>

      <path class="band" d="M0,73 C180,73 260,0 374,0 C488,0 568,73 748,73 V247 C568,247 488,320 374,320 C260,320 180,247 0,247 Z"/>

      <ellipse class="oval-rim" cx="374" cy="158" rx="97" ry="160"/>
      <ellipse class="oval-face" cx="374" cy="158" rx="88" ry="150" fill="url(#copperFoil)"/>

      <g class="back-info" text-anchor="middle">
        <text class="info-text info-strong" x="129" y="123">KELV™</text>
        <text class="info-text" x="129" y="140">77 MAPLE ROAD</text>
        <text class="info-text" x="129" y="156">YOUR CITY, AB 03456</text>
        <text class="info-text" x="129" y="172">U.S.A.</text>
        <text class="info-text" x="129" y="200"><tspan class="info-strong">Exp:</tspan> January 2020</text>
      </g>

      <g class="front-panel" text-anchor="middle">
        <text class="brand-name" x="374" y="118">KELV</text>
        <line class="rule" x1="309" y1="146" x2="439" y2="146"/>
        <text class="skin-type" x="374" y="171">DRY SKIN</text>
        <line class="rule" x1="309" y1="180" x2="439" y2="180"/>
        <text class="product-name" x="374" y="222">BEARD</text>
        <text class="product-name" x="374" y="254">OIL</text>
        <text class="volume" x="374" y="293">30ml</text>
      </g>

      <g class="ingredients" text-anchor="middle">
        <text class="info-text info-strong" x="610" y="128">Ingrédients :</text>
        <text class="info-text" x="610" y="145">Simmondsia chinensis (Jojoba)</text>
        <text class="info-text" x="610" y="162">Seed Oil*, Corylus avellana</text>
        <text class="info-text" x="610" y="179">(Hazelnut) Oil*, Vitis vinifera</text>
        <text class="info-text" x="610" y="196">Seed Oil*, Trocopherol, parfum.</text>
      </g>
    </svg>
  </div>
</div>
</body>
</html>
```